'We're just a little bit different' business cards for an IT Startup

We are an Information Technology Start-up focusing on providing IT strategy services to large midcap and enterprise organisations. We need to create business cards which reflect us personally and our brand. Clarvane.io is looking to differentiate itself in the market by providing IT strategy that reflects Information technology today.
We would like business cards that:
- Are just a little bit different, so people read them
- Reflect that Clarvane.Io is a modern disruptive technology company
- Reinforces our brand – strategy reinvented
- Provides information about us that is deeper and richer than just here’s my mobile and email address. We’d like the business card to be a snapshot of who we individually. It might be fav movie, book, sports, favourite beer, my family etc, fav quote etc

I have attached a document which has details about me to use on a sample business card and it also includes snapshots of our website. Also attached is our logo. If you need more information please ask

Industry/Entity Type

Information Technology

Beacon Information for Business Card

See attached document, for my personal details to use as a sample

Requirements
Must have
• my details
• web site - url clarvane.io
• something a little bit different
Nice to have
• I'd like to see the design incorporate information about us that lets them see us as fellow human beings not just a work person
Should not have
• standard bland business cards

```html
<!DOCTYPE html>
<html lang="en">
<head>
<meta charset="utf-8">
<title>Clarvane.io business cards</title>
<link rel="stylesheet" href="https://fonts.googleapis.com/css2?family=Roboto:ital,wght@0,400;1,400&family=Roboto+Condensed:wght@400&family=Open+Sans:wght@400;700&display=swap">
<style>
  :root {
    --backdrop: #aaa8a9;
    --card: #4d5964;
    --bubble: #5d7382;
    --accent: #4ba5e2;
    --ink: #ffffff;
    --ink-soft: #e6ebef;
  }
  html, body { margin: 0; padding: 0; width: 1200px; height: 1200px; overflow: hidden; }
  body { background: var(--backdrop); position: relative; font-family: "Roboto", Arial, sans-serif; color: var(--ink); }

  .card { position: absolute; width: 712px; height: 418px; background: var(--card); overflow: hidden; }
  .card--back { left: 238px; top: 118px; }
  .card--front { left: 231px; top: 643px; }

  .bubble { position: absolute; border-radius: 50%; background: var(--bubble); }
  .card--back .bubble { left: 382px; top: 32px; width: 300px; height: 300px; opacity: .85; }
  .card--front .bubble { left: 385px; top: 26px; width: 300px; height: 300px; }

  /* back: about-me lines */
  .fact { position: absolute; box-sizing: border-box; border: 1.5px solid var(--ink); border-radius: 8px;
          display: flex; align-items: center; justify-content: center; text-align: center;
          font-size: 17px; line-height: 22px; color: var(--ink); }
  .fact--family { left: 195px; top: 30px; width: 375px; height: 35px; }
  .fact--hobbies { left: 29px; top: 82px; width: 603px; height: 33px; }
  .fact--quote { left: 42px; top: 130px; width: 640px; height: 65px; padding: 0 30px 16px; line-height: 22px; }
  .fact--values { left: 150px; top: 217px; width: 467px; height: 52px; text-align: left; justify-content: flex-start; padding-left: 17px; }
  .fact--film { left: 62px; top: 286px; width: 558px; height: 33px; }
  .fact--music { left: 52px; top: 335px; width: 632px; height: 58px; font-family: "Roboto Condensed", Arial, sans-serif;
                 font-size: 16.5px; text-align: left; justify-content: flex-start; padding-left: 36px; }
  .quote-author { position: absolute; right: 36px; top: 183px; padding: 0 8px; background: var(--card);
                  font-style: italic; font-size: 16px; color: var(--accent); }

  .icon { position: absolute; }
  .icon-placeholder { position: absolute; border-radius: 10px; background: var(--accent); opacity: .75; }
  .icon-placeholder--family { left: 143px; top: 25px; width: 44px; height: 46px; }
  .icon-placeholder--bike { left: 626px; top: 70px; width: 56px; height: 46px; }
  .icon-placeholder--film { left: 611px; top: 283px; width: 42px; height: 40px; }

  /* front */
  .brand { position: absolute; left: 50px; top: 52px; display: flex; align-items: center; gap: 10px; }
  .brand__dot { width: 20px; height: 20px; border-radius: 50%; background: var(--accent); }
  .brand__name { font-family: "Open Sans", Arial, sans-serif; font-weight: 700; font-size: 56px; letter-spacing: -1.5px; color: var(--ink); line-height: 1; }

  .person { position: absolute; left: 385px; top: 148px; width: 300px; text-align: center; font-family: "Open Sans", Arial, sans-serif; }
  .person__name { font-weight: 700; font-size: 30px; line-height: 36px; }
  .person__role { font-size: 16px; color: var(--ink-soft); margin-top: 2px; }

  .contact { position: absolute; left: 46px; top: 305px; margin: 0; padding: 0; list-style: none; }
  .contact li { display: flex; align-items: center; height: 25px; font-size: 18.5px; color: var(--ink); }
  .contact svg { width: 18px; height: 18px; margin-right: 17px; }
</style>
</head>
<body>

<section class="card card--back" aria-label="Card back: about Owen">
  <div class="bubble"></div>

  <div class="icon-placeholder icon-placeholder--family" role="img" aria-label="Family icon"></div>
  <div class="fact fact--family">Elena my wife of 21 years and 4 children</div>

  <div class="fact fact--hobbies">Riding bikes, windsurfing, squash, running, reading, writing, tinkering</div>
  <div class="icon-placeholder icon-placeholder--bike" role="img" aria-label="Bicycle icon"></div>

  <svg class="icon" style="left:27px;top:134px" width="42" height="36" viewBox="0 0 42 36" fill="none" stroke="#4ba5e2" stroke-width="2.5" stroke-linejoin="round">
    <path d="M3 18 C3 8 8 3 17 2 V8 C12 9 10 12 10 16 H17 V33 H3 Z"/>
    <path d="M23 18 C23 8 28 3 37 2 V8 C32 9 30 12 30 16 H37 V33 H23 Z"/>
  </svg>
  <div class="fact fact--quote">"Don't only practice your art but force your way into its secrets for it and knowledge can raise men to the Devine"</div>
  <span class="quote-author">Anselm Richter</span>

  <svg class="icon" style="left:94px;top:217px" width="58" height="50" viewBox="0 0 58 50" fill="none" stroke="#4ba5e2" stroke-width="3.5" stroke-linejoin="round">
    <path d="M29 46 C14 34 3 26 3 15 C3 8 9 3 16 3 C22 3 26 7 29 11 C32 7 36 3 42 3 C49 3 55 8 55 15 C55 26 44 34 29 46 Z"/>
  </svg>
  <div class="fact fact--values">We can't all be a Varenko however, whatever our gift<br>I believe we should create beauty in all that we do</div>

  <div class="fact fact--film">Beacon - Edwin Marlow's masterpiece brought to life, oozes hope</div>
  <div class="icon-placeholder icon-placeholder--film" role="img" aria-label="Film clapperboard icon"></div>

  <svg class="icon" style="left:27px;top:334px" width="48" height="50" viewBox="0 0 48 50" fill="none" stroke="#4ba5e2" stroke-width="2.5">
    <ellipse cx="10" cy="41" rx="7" ry="5.5"/>
    <ellipse cx="37" cy="35" rx="7" ry="5.5"/>
    <path d="M17 41 V10 L44 3 V35"/>
    <path d="M17 17 L44 10"/>
  </svg>
  <div class="fact fact--music">Violet Harbour and Tomas Reyes – Heavily influential in my formative years, their<br>mastery and creativity within their profession is something I strive to mimic in mine</div>
</section>

<section class="card card--front" aria-label="Card front">
  <div class="bubble"></div>

  <div class="brand">
    <span class="brand__dot"></span>
    <span class="brand__name">Clarvane</span>
  </div>

  <div class="person">
    <div class="person__name">Owen Hartley</div>
    <div class="person__role">Founder</div>
  </div>

  <ul class="contact">
    <li>
      <svg viewBox="0 0 18 18" fill="#4ba5e2"><path d="M2 6 C2 3 5 2 9 2 C13 2 16 3 16 6 H12 V5 H6 V6 Z"/><rect x="3" y="8" width="12" height="8" rx="1.5"/></svg>
      0400372918
    </li>
    <li>
      <svg viewBox="0 0 18 18" fill="none" stroke="#4ba5e2" stroke-width="1.6"><circle cx="9" cy="9" r="7"/><ellipse cx="9" cy="9" rx="3" ry="7"/><path d="M2 9 H16 M3.5 5 H14.5 M3.5 13 H14.5"/></svg>
      www.clarvane.io
    </li>
    <li>
      <svg viewBox="0 0 18 18" fill="none" stroke="#4ba5e2" stroke-width="1.6"><rect x="2" y="4" width="14" height="10" rx="1"/><path d="M2 4 L9 10 L16 4 M2 14 L7 8.5 M16 14 L11 8.5"/></svg>
      owen@clarvane.io
    </li>
  </ul>
</section>

</body>
</html>
```